4 Poster Designs required for Nail Salon

We require 4 poster designs that will be displayed inside a shopping centre. Each design should contain our logo and the words "Located next to Tallora" (or similar). Design 1 (MOTHERS DAY) should contain the words "Mothers Day Special" and "$10 gift voucher when you spend over $50". Design 2 (CHRISTMAS) should contain the words "Christmas in July" and "Purchase a set of nails and get a $10 gift voucher". Design 3 (ALL YEAR) should contain the words "New Deluxe Spa Pedicure Service" and the words "Try our new Deluxe Spa Pedicure and get a free nail buff, shape and polish for your fingernails". Design 4 (ALL YEAR 2)should contain high quality nail salon image(s) and the words "Now Open". We like designs that support our image of high quality/fun/clean and safe.
Updates
I will close this early. In 24 hours.
Target Market(s)
Rich mums
Industry/Entity Type
Shopping
Look and feel
Each slider illustrates characteristics of the customer's brand and the style your logo design should communicate.

```html
<!DOCTYPE html>
<html lang="en">
<head>
<meta charset="utf-8">
<title>Glossa Nail Salon – Christmas in July</title>
<link rel="stylesheet" href="https://fonts.googleapis.com/css2?family=Questrial&family=Open+Sans:ital,wght@0,700;0,800;1,800&family=Playfair+Display:wght@900&display=swap">
<style>
  :root {
    --canvas-bg: #ffffff;
    --brand-pink: #e0559f;
    --brand-pink-light: #ec9cc6;
    --title-pink: #e6287f;
    --band-red: #d6262c;
    --band-red-light: #e8484c;
    --badge-purple: #7a2a9a;
    --badge-magenta: #b42a9e;
    --white: #ffffff;
  }
  * { margin: 0; padding: 0; box-sizing: border-box; }
  html, body { width: 848px; height: 1200px; overflow: hidden; background: var(--canvas-bg); }
  .poster { position: relative; width: 848px; height: 1200px; overflow: hidden; }

  .backdrop {
    position: absolute; left: 0; top: 0; width: 848px; height: 590px;
    background:
      radial-gradient(circle at 20% 40%, rgba(245,170,70,0.75), transparent 55%),
      radial-gradient(circle at 90% 55%, rgba(140,200,230,0.6), transparent 45%),
      radial-gradient(circle at 70% 75%, rgba(240,150,200,0.55), transparent 45%),
      linear-gradient(180deg, #fffdf6 0%, #fdeedd 45%, #f8d9c8 100%);
  }

  .festive-scene {
    position: absolute; left: 0; top: 719px; width: 848px; height: 481px;
    background:
      radial-gradient(ellipse at 50% 55%, rgba(222,200,140,0.95), transparent 35%),
      radial-gradient(circle at 18% 55%, rgba(190,30,35,0.9), transparent 22%),
      radial-gradient(circle at 72% 45%, rgba(200,35,40,0.9), transparent 25%),
      linear-gradient(180deg, #f4ece2 0%, #c9a77a 40%, #b8342f 70%, #f3ece4 100%);
  }

  .logo {
    position: absolute; left: 493px; top: 27px; width: 326px; height: 143px;
    background: linear-gradient(90deg, var(--brand-pink), var(--brand-pink-light));
    color: var(--white);
    font-family: "Questrial", sans-serif;
    display: flex; flex-direction: column; align-items: flex-end; justify-content: center;
    padding-right: 48px;
  }
  .logo-name { font-size: 46px; letter-spacing: 5px; line-height: 1; }
  .logo-tag { font-size: 15px; letter-spacing: 1px; margin-top: 4px; }

  .headline {
    position: absolute; left: 113px; top: 268px; white-space: nowrap;
    font-family: "Questrial", sans-serif; font-weight: 400; font-size: 76px; line-height: 1;
    color: var(--title-pink);
  }

  .offer-band {
    position: absolute; left: 0; top: 583px; width: 848px; height: 136px;
    background: linear-gradient(180deg, var(--band-red) 0%, var(--band-red-light) 100%);
  }
  .offer-text {
    position: absolute; left: 294px; top: 596px; white-space: nowrap;
    font-family: "Open Sans", sans-serif; font-weight: 800; font-style: italic;
    font-size: 49px; line-height: 64px; color: var(--white);
  }

  .voucher-badge { position: absolute; left: 32px; top: 530px; width: 240px; height: 240px; }
  .voucher-label {
    position: absolute; left: 32px; top: 530px; width: 240px; height: 240px;
    display: flex; flex-direction: column; align-items: center; justify-content: center;
    font-family: "Open Sans", sans-serif; color: var(--white);
  }
  .voucher-amount { font-size: 66px; line-height: 1; font-weight: 800; }
  .voucher-caption { font-size: 27px; line-height: 1.3; font-weight: 700; }

  .location {
    position: absolute; left: 0; width: 848px; top: 1082px; text-align: center; white-space: nowrap;
    font-family: "Playfair Display", serif; font-weight: 900; font-size: 36px;
    letter-spacing: 6px; color: var(--white);
  }
</style>
</head>
<body>
<main class="poster">
  <div class="backdrop" role="img" aria-label="Soft warm gradient with glowing bokeh circles and purple swirl flourishes"></div>
  <div class="festive-scene" role="img" aria-label="Red Christmas baubles, a glittering gold star, pine branches and gold ribbon"></div>

  <div class="logo">
    <span class="logo-name">Glossa</span>
    <span class="logo-tag">Nail Salon</span>
  </div>

  <h1 class="headline">Christmas in July</h1>

  <div class="offer-band"></div>
  <p class="offer-text">when you Purchase<br>a set of nails</p>

  <svg class="voucher-badge" viewBox="0 0 240 240" aria-hidden="true">
    <defs>
      <linearGradient id="badgeFill" x1="0" y1="0" x2="0" y2="1">
        <stop offset="0" stop-color="var(--badge-purple)"/>
        <stop offset="1" stop-color="var(--badge-magenta)"/>
      </linearGradient>
    </defs>
    <circle cx="120" cy="120" r="106" fill="var(--white)"/>
    <circle cx="120" cy="120" r="108" fill="none" stroke="var(--white)" stroke-width="20" stroke-linecap="round" stroke-dasharray="0 24.23"/>
    <circle cx="120" cy="120" r="98" fill="url(#badgeFill)"/>
    <circle cx="120" cy="120" r="100" fill="none" stroke="url(#badgeFill)" stroke-width="12" stroke-linecap="round" stroke-dasharray="0 22.44"/>
  </svg>
  <div class="voucher-label">
    <span class="voucher-amount">$10</span>
    <span class="voucher-caption">Gift voucher</span>
  </div>

  <p class="location">Located next to Tallora</p>
</main>
</body>
</html>
```